Need bold & innovative new PPT design

Our logo/branding is being designed at the moment on this site.We are a Minerals and Mining Industry Association which has mining companies as its members. We do collaborate research with research companies, universities and scientific bodies to bring projects which benefit the mining industry. We are an international company which started 60 years ago and want a renewal/rejuvenation of our brand.

Target Market(s)

Mining & Minerals Industry. Scientists, and scientific research organisations.

Industry/Entity Type

Mining

Requirements
Must have
• Bold designs and colours. I have attached an old version of our template (with dated colours & logo). Please use new logo (attached) and it's colours.
• NOTE: There may be some confusion - we only need 2 slides. The title slide & the normal presentation pages. Thanks
Nice to have
• Red & Blue as according to our new logo and websites are preferred.
• New logo attached. New website: http://quorvane-assoc.net/
Should not have
• Yellow! We're quite sick of that.

```html
<!DOCTYPE html>
<html lang="en">
<head>
<meta charset="utf-8">
<title>Corvath International – Presentation Template</title>
<link rel="stylesheet" href="https://fonts.googleapis.com/css2?family=PT+Sans+Narrow:wght@400;700&family=PT+Sans:ital,wght@0,400;1,400&display=swap">
<style>
  :root{
    --stage:#1b2028;
    --blue-deep:#0b3f7a;
    --blue-mid:#1a5fa6;
    --blue-light:#2a74bd;
    --heading-blue:#1c4f8a;
    --red:#c41f2c;
    --red-dark:#9e1520;
    --paper:#eef7fb;
    --paper-2:#d7ecf5;
    --ink:#1f2a3a;
    --white:#ffffff;
    --mark:#1d56a0;
  }
  *{box-sizing:border-box;margin:0;padding:0}
  html,body{width:1200px;height:900px;overflow:hidden}
  body{background:var(--stage);position:relative;font-family:"PT Sans Narrow",sans-serif;color:var(--ink)}

  .slide{position:absolute;width:586px;height:440px;overflow:hidden;
    background:linear-gradient(180deg,var(--paper) 0%,var(--paper-2) 100%)}
  .slide--one{left:10px;top:8px}
  .slide--two{left:604px;top:8px}
  .slide--three{left:10px;top:452px}
  .slide--four{left:604px;top:452px}

  .slide-header{position:absolute;left:0;top:0;width:100%;height:44px;
    background:linear-gradient(180deg,var(--blue-light),var(--blue-deep));
    border-bottom:2px solid var(--red);
    color:var(--white);font-weight:700;font-size:24px;text-align:center;line-height:42px}

  .slide-footer{position:absolute;left:0;bottom:0;width:100%;height:42px;
    background:linear-gradient(180deg,var(--blue-mid),var(--blue-deep));
    border-top:2px solid var(--red)}
  .slide-number{position:absolute;left:16px;top:7px;width:30px;height:28px;
    background:var(--red);border:1px solid var(--red-dark);color:var(--white);
    font-family:"PT Sans",sans-serif;font-size:17px;line-height:26px;text-align:center}
  .footer-text{position:absolute;left:64px;top:0;line-height:40px;color:var(--white);
    font-family:"PT Sans",sans-serif;font-style:italic;font-size:14px}
  .footer-date{left:92px;font-size:15px}
  .nav{position:absolute;top:7px;height:28px;background:linear-gradient(180deg,#d7303b,var(--red-dark));
    color:var(--white);font-family:"PT Sans",sans-serif;font-size:12.5px;line-height:28px;text-align:center}
  .nav--next{right:14px;width:48px;padding-right:6px;clip-path:polygon(0 0,82% 0,100% 50%,82% 100%,0 100%);border-radius:4px 0 0 4px}
  .nav--back{right:70px;width:50px;padding-left:6px;clip-path:polygon(18% 0,100% 0,100% 100%,18% 100%,0 50%);border-radius:0 4px 4px 0}

  .cover-band{position:absolute;left:0;top:0;width:100%;height:257px;
    background:radial-gradient(ellipse at 50% 40%,var(--blue-light) 0%,var(--blue-deep) 85%);
    border-bottom:4px solid var(--red)}
  .cover-title{position:absolute;top:100px;width:100%;text-align:center;color:var(--white);font-weight:700;font-size:38px}
  .cover-subtitle{position:absolute;top:156px;left:100px;width:386px;text-align:center;color:var(--white);font-size:15.5px;line-height:21px}
  .cover-body{position:absolute;left:0;top:261px;width:100%;height:135px;background:linear-gradient(180deg,#fff,#eef3f8)}

  .brand{position:absolute;display:flex;align-items:center;gap:8px;color:var(--mark);font-weight:700;line-height:1}
  .brand-dot{border-radius:50%;background:var(--mark)}
  .brand--cover{left:205px;top:306px;font-size:30px}
  .brand--cover .brand-dot{width:20px;height:20px}
  .brand--corner{right:14px;bottom:60px;font-size:19px}
  .brand--corner .brand-dot{width:13px;height:13px}
  .brand--faint{left:126px;top:150px;font-size:56px;color:#bcd6e6;gap:14px}
  .brand--faint .brand-dot{width:36px;height:36px;background:#bcd6e6}
  .brand--faint-small{left:100px;top:140px;font-size:48px;color:#d6e8f1;gap:12px}
  .brand--faint-small .brand-dot{width:30px;height:30px;background:#d6e8f1}
  .brand-name small{display:block;font-size:.55em;letter-spacing:.18em;margin-top:3px}

  .content{position:absolute;left:43px;top:72px}
  .content-heading{color:var(--heading-blue);font-weight:700;font-size:18px;margin-bottom:7px}
  .checklist{list-style:none}
  .checklist li{position:relative;padding-left:23px;font-size:13.2px;line-height:19px;color:var(--ink)}
  .checklist li svg{position:absolute;left:0;top:2px}
  .checklist--wide{width:480px}

  .team-photo{position:absolute;left:206px;top:92px;width:356px;height:296px;
    background:linear-gradient(180deg,#7d8797 0%,#5a6474 45%,#c9d8e3 78%,rgba(238,247,251,0) 100%);
    border-radius:4px}
</style>
</head>
<body>

<svg width="0" height="0" style="position:absolute">
  <symbol id="tick" viewBox="0 0 14 14">
    <rect x="1" y="3" width="10" height="10" fill="none" stroke="#2b3a4c" stroke-width="1.2"/>
    <path d="M3 7.5l2.6 2.8L13 1.5" fill="none" stroke="#1f7a3a" stroke-width="2"/>
  </symbol>
</svg>

<section class="slide slide--one">
  <div class="cover-band">
    <h1 class="cover-title">Project Title Here</h1>
    <p class="cover-subtitle">Subtext here Subtext here Subtext here Subtext here Subtext here Subtext here Subtext here Subtext here</p>
  </div>
  <div class="cover-body">
    <div class="brand brand--cover"><span class="brand-dot"></span><span class="brand-name">Corvath International</span></div>
  </div>
  <footer class="slide-footer">
    <span class="slide-number">01</span>
    <span class="footer-text footer-date">01/02/15</span>
    <span class="nav nav--next">Start</span>
  </footer>
</section>

<section class="slide slide--two">
  <header class="slide-header">Slide Title</header>
  <div class="brand brand--faint"><span class="brand-dot"></span><span class="brand-name">Corvath International</span></div>
  <div class="brand brand--corner"><span class="brand-dot"></span><span class="brand-name">Corvath International</span></div>
  <footer class="slide-footer">
    <span class="slide-number">02</span>
    <span class="footer-text">Tagline/Slogan about Your Company</span>
    <span class="nav nav--back">Back</span>
    <span class="nav nav--next">Next</span>
  </footer>
</section>

<section class="slide slide--three">
  <header class="slide-header">Slide Title</header>
  <div class="brand brand--faint-small"><span class="brand-dot"></span><span class="brand-name">Corvath International</span></div>
  <div class="content">
    <h2 class="content-heading">Something About Your Business</h2>
    <ul class="checklist checklist--wide">
      <li><svg width="14" height="14"><use href="#tick"/></svg>High volume local boutique real estate company</li>
      <li><svg width="14" height="14"><use href="#tick"/></svg>Specialize in selling homes throughout the San Francisco Bay Area</li>
      <li><svg width="14" height="14"><use href="#tick"/></svg>Focus on modern marketing techniques and thinking outside the box</li>
      <li><svg width="14" height="14"><use href="#tick"/></svg>“High Tech and High Touch” approach to real estate</li>
      <li><svg width="14" height="14"><use href="#tick"/></svg>Certified Green Business Everything is done and stored online. No File Cabinets in our offices!</li>
      <li><svg width="14" height="14"><use href="#tick"/></svg>Exceptional web presence far beyond other local real estate companies</li>
      <li><svg width="14" height="14"><use href="#tick"/></svg>Clean, streamline, and hip marketing materials</li>
      <li><svg width="14" height="14"><use href="#tick"/></svg>A company constantly looking into the latest real estate trends, tools, and technology to better assist their agents and clients sell homes in the modern world, all while embracing tried and true real estate values and practices as well</li>
      <li><svg width="14" height="14"><use href="#tick"/></svg>Leading authority for architectural homes and recognized world wide</li>
      <li><svg width="14" height="14"><use href="#tick"/></svg>Not Just Modern Homes! We focus on Modern Real Estate<br>Practices through and through.</li>
    </ul>
  </div>
  <div class="brand brand--corner"><span class="brand-dot"></span><span class="brand-name">Corvath International</span></div>
  <footer class="slide-footer">
    <span class="slide-number">03</span>
    <span class="footer-text">Tagline/Slogan about Your Company</span>
    <span class="nav nav--back">Back</span>
    <span class="nav nav--next">Next</span>
  </footer>
</section>

<section class="slide slide--four">
  <header class="slide-header">Slide Title</header>
  <div class="brand brand--faint-small"><span class="brand-dot"></span><span class="brand-name">Corvath International</span></div>
  <div class="team-photo" role="img" aria-label="Photograph of a large group of business professionals and tradespeople standing together"></div>
  <div class="content">
    <h2 class="content-heading">Our Services</h2>
    <ul class="checklist">
      <li><svg width="14" height="14"><use href="#tick"/></svg>Handymen</li>
      <li><svg width="14" height="14"><use href="#tick"/></svg>Contractors</li>
      <li><svg width="14" height="14"><use href="#tick"/></svg>Stagers</li>
      <li><svg width="14" height="14"><use href="#tick"/></svg>Painters</li>
      <li><svg width="14" height="14"><use href="#tick"/></svg>Cleaners</li>
      <li><svg width="14" height="14"><use href="#tick"/></svg>Movers</li>
      <li><svg width="14" height="14"><use href="#tick"/></svg>Storage companies</li>
      <li><svg width="14" height="14"><use href="#tick"/></svg>Landscapers</li>
      <li><svg width="14" height="14"><use href="#tick"/></svg>Estate Sale Professionals</li>
      <li><svg width="14" height="14"><use href="#tick"/></svg>Lawyers</li>
      <li><svg width="14" height="14"><use href="#tick"/></svg>Mortgage Brokers</li>
      <li><svg width="14" height="14"><use href="#tick"/></svg>Inspectors</li>
    </ul>
  </div>
  <div class="brand brand--corner"><span class="brand-dot"></span><span class="brand-name">Corvath International</span></div>
  <footer class="slide-footer">
    <span class="slide-number">04</span>
    <span class="footer-text">Tagline/Slogan about Your Company</span>
    <span class="nav nav--back">Back</span>
    <span class="nav nav--next">Next</span>
  </footer>
</section>

</body>
</html>
```